Online Psychology Practice needs business cards.

Online Psychology service needs business cards. Have own logo- please see uploaded. I have other file formats if you need (not sure one needed?)

Details for Business Card:
Fiona Kettlewood
Clinical Psychologist BPsych, BPsych (Hons), MPsych (Clin), MAPS
T: 0457260714 | F: 08 71526804
E: hello@harbourlightmindcarestudio.com.au
W: harbourlightmindcarestudio.com.au

Industry/Entity Type

Health

Contact Information for Business Card

Logo plus details above (couldn't write in this section)

```html
<!DOCTYPE html>
<html lang="en">
<head>
<meta charset="utf-8">
<title>Harbourlight Mindcare Studio – Business Card</title>
<link href="https://fonts.googleapis.com/css2?family=Cinzel:wght@700&family=Noto+Sans:wght@400&display=swap" rel="stylesheet">
<style>
  :root {
    --backdrop: #808080;
    --card-white: #ffffff;
    --navy: #175a82;
    --teal: #0b8aa8;
    --text-grey: #737373;
    --grad-light: #0d8ca8;
    --grad-dark: #155f89;
  }
  * { box-sizing: border-box; margin: 0; padding: 0; }
  html, body { width: 1093px; height: 1200px; overflow: hidden; }
  body {
    background: var(--backdrop);
    position: relative;
    font-family: "Noto Sans", sans-serif;
  }
  .card {
    position: absolute;
    left: 264px;
    width: 580px;
    height: 357px;
    overflow: hidden;
  }
  .card--front { top: 226px; background: var(--card-white); }
  .card--back {
    top: 620px;
    background: linear-gradient(155deg, var(--grad-light) 0%, var(--grad-light) 35%, var(--grad-dark) 100%);
    display: flex;
    flex-direction: column;
    align-items: center;
    justify-content: center;
    gap: 34px;
  }
  .brand-accent {
    position: absolute;
    right: -150px;
    top: -20px;
    width: 430px;
    height: 400px;
    background: radial-gradient(ellipse at 62% 50%, var(--teal) 0%, var(--navy) 38%, rgba(23, 90, 130, 0.35) 58%, rgba(255, 255, 255, 0) 72%);
  }
  .brand-name {
    font-family: "Cinzel", serif;
    font-weight: 700;
    text-transform: uppercase;
    line-height: 1.25;
  }
  .card--front .brand-name {
    position: absolute;
    left: 27px;
    top: 46px;
    font-size: 21px;
    letter-spacing: 2.6px;
    color: var(--navy);
  }
  .card--back .brand-name {
    font-size: 25px;
    letter-spacing: 3.2px;
    color: var(--card-white);
    text-align: center;
  }
  .brand-dot {
    width: 78px;
    height: 78px;
    border-radius: 50%;
    background: var(--card-white);
  }
  .person-name {
    position: absolute;
    left: 23px;
    top: 142px;
    font-family: "Cinzel", serif;
    font-weight: 700;
    font-size: 23px;
    text-transform: uppercase;
    color: var(--navy);
  }
  .credentials {
    position: absolute;
    left: 23px;
    top: 180px;
    font-size: 15.5px;
    line-height: 18px;
    color: var(--teal);
  }
  .contact-list {
    position: absolute;
    left: 21px;
    top: 229px;
    list-style: none;
  }
  .contact-item {
    display: flex;
    align-items: center;
    gap: 7px;
    height: 22px;
    font-size: 15px;
    letter-spacing: 1px;
    color: var(--text-grey);
  }
  .contact-icon { width: 15px; height: 15px; fill: var(--navy); flex: none; }
</style>
</head>
<body>
  <section class="card card--front" aria-label="Business card front">
    <div class="brand-accent" role="img" aria-label="Brand colour accent"></div>
    <p class="brand-name">Harbourlight<br>Mindcare Studio</p>
    <h1 class="person-name">Fiona Kettlewood</h1>
    <p class="credentials">Clinical Psychologist BPsych<br>BPsych (Hons), MPsych (Clin), MAPS</p>
    <ul class="contact-list">
      <li class="contact-item">
        <svg class="contact-icon" viewBox="0 0 16 16" aria-hidden="true"><path d="M3.5 1 L6 1 L7 4.5 L5.4 5.8 C6.3 7.8 8.2 9.7 10.2 10.6 L11.5 9 L15 10 L15 12.5 C15 13.9 13.9 15 12.5 15 C6.7 15 1 9.3 1 3.5 C1 2.1 2.1 1 3.5 1Z"/></svg>
        0457260714
      </li>
      <li class="contact-item">
        <svg class="contact-icon" viewBox="0 0 16 16" aria-hidden="true"><path d="M4 1h8v4H4z M1 6h14v6h-2v-2H3v2H1z M4 11h8v4H4z"/></svg>
        08 71526804
      </li>
      <li class="contact-item">
        <svg class="contact-icon" viewBox="0 0 16 16" aria-hidden="true"><path d="M1 3h14v10H1z" fill="none" stroke="var(--navy)" stroke-width="1.6"/><path d="M1 3l7 6 7-6" fill="none" stroke="var(--navy)" stroke-width="1.6"/></svg>
        hello@harbourlightmindcarestudio.com.au
      </li>
      <li class="contact-item">
        <svg class="contact-icon" viewBox="0 0 16 16" aria-hidden="true"><g fill="none" stroke="var(--navy)" stroke-width="1.3"><circle cx="8" cy="8" r="6.7"/><ellipse cx="8" cy="8" rx="3" ry="6.7"/><path d="M1.3 8h13.4 M2.5 4.5h11 M2.5 11.5h11"/></g></svg>
        harbourlightmindcarestudio.com.au
      </li>
    </ul>
  </section>

  <section class="card card--back" aria-label="Business card back">
    <div class="brand-dot" aria-hidden="true"></div>
    <p class="brand-name">Harbourlight<br>Mindcare Studio</p>
  </section>
</body>
</html>
```